Bright Path Attorneys Billboard Design for Personal Injury Law Firm

Need a billboard design that we can use for different versions. 1400px X 400px jpeg or png
I have attached the logo and the attorney for the billboard. Attorney Marla Benning
Here is a link to our current website brightpathlegalgroup.example

HEADLINE: HIT BY A TRUCK?
SUBHEAD: NO FEE. BIG FIGHT.
877-GRANTLY

HEADLINE: ACCIDENT?
SUBHEAD: NO FEE, UNLESS WE WIN!
877-GRANTLY

HEADLINE: BIG TRUCK. BIG CASE.
SUBHEAD: YOU PAY $0 UPFRONT
877-GRANTLY

Target Market(s)

People in Car Accident

Industry/Entity Type

Personal Injury Attorneys

```html
<!DOCTYPE html>
<html lang="en">
<head>
<meta charset="utf-8">
<title>Bright Path Attorneys Billboard</title>
<link rel="stylesheet" href="https://fonts.googleapis.com/css2?family=Oswald:wght@700&family=Montserrat:wght@700;800&display=swap">
<style>
  :root {
    --navy: #0c4166;
    --navy-ink: #0d3a5c;
    --gold: #f8c11a;
    --white: #ffffff;
    --page: #ffffff;
    --portrait-top: #c9a27c;
    --portrait-bottom: #1c2a44;
  }
  html, body {
    margin: 0;
    width: 1027px;
    height: 1200px;
    overflow: hidden;
    background: var(--page);
  }
  .billboard {
    position: absolute;
    left: 33px;
    top: 400px;
    width: 960px;
    height: 400px;
    box-shadow: 0 10px 28px rgba(0, 0, 0, 0.35);
  }
  .billboard svg { display: block; }
  .headline {
    font-family: "Oswald", "Arial Narrow", sans-serif;
    font-weight: 700;
    fill: var(--white);
  }
  .subhead {
    font-family: "Montserrat", Arial, sans-serif;
    font-weight: 800;
    fill: var(--navy-ink);
  }
  .phone {
    font-family: "Montserrat", Arial, sans-serif;
    font-weight: 800;
    fill: var(--gold);
  }
  .firm-name {
    font-family: "Montserrat", Arial, sans-serif;
    font-weight: 700;
    fill: var(--white);
  }
  .stripe, .sub-band, .firm-dot { fill: var(--gold); }
  .panel { fill: var(--navy); }
</style>
</head>
<body>
  <div class="billboard">
    <svg width="960" height="400" viewBox="0 0 960 400">
      <defs>
        <linearGradient id="portrait-tone" x1="0" y1="0" x2="0" y2="1">
          <stop offset="0" stop-color="var(--portrait-top)"/>
          <stop offset="0.4" stop-color="#b88e6a"/>
          <stop offset="1" stop-color="var(--portrait-bottom)"/>
        </linearGradient>
      </defs>
      <rect class="panel" x="0" y="0" width="960" height="400"/>
      <polygon class="stripe" points="193,0 292,0 0,362 0,240"/>
      <rect class="sub-band" x="214" y="163" width="746" height="89"/>

      <path class="portrait" fill="url(#portrait-tone)" role="img"
            aria-label="Portrait of attorney Marla Benning in a navy blazer, arms crossed"
            d="M 22,90 Q 30,34 110,32 Q 190,34 200,90 L 206,256 Q 290,268 296,300 L 296,400 L 22,400 Z"/>

      <text class="headline" x="255" y="130" font-size="104" textLength="675" lengthAdjust="spacingAndGlyphs">HIT BY A TRUCK?</text>
      <text class="subhead" x="285" y="227" font-size="58" textLength="595" lengthAdjust="spacingAndGlyphs">NO FEE. BIG FIGHT.</text>
      <text class="phone" x="304" y="338" font-size="78" textLength="500" lengthAdjust="spacingAndGlyphs">877-GRANTLY</text>

      <rect class="firm-dot" x="848" y="340" width="9" height="9"/>
      <text class="firm-name" x="861" y="348" font-size="10" textLength="88" lengthAdjust="spacingAndGlyphs">Bright Path Attorneys</text>
    </svg>
  </div>
</body>
</html>
```